Digital Marketing Agency Landing Page

At VELMIT, we offer a comprehensive solution for solar companies' client acquisition needs in the rapidly growing industry. We handle end-to-end client acquisition, meaning we manage the entire lifecycle of capturing new clients—from initial lead generation to delivering the ready-to-buy homeowner. Our expertise in targeted advertising, data analytics, and customer relationship management ensures that we not only find potential customers but also nurture them through tailored engagement strategies until they are ready to make a purchase. By entrusting us with your client acquisition process, solar companies can focus on what they do best—providing sustainable energy solutions—while we work behind the scenes to grow your customer base and increase your market share.

We need to restructure our website to make it more professional. We don't need any complex functionalities. We are looking for someone that is good in design and can build a visually aesthetic website following our brand image. We only need a landing page and a lead form in the end. I would like to have only one page, but a relatively big one where people scroll down. I would like to have a minimal and classy look. Something that is timeless and elegant.

Structure:

initial page
About us
How we operate
Get in touch

Target Market(s)

Solar Comapanies

Industry/Entity Type

Marketing solautions

Coding

Coded - Design and coding required

Number of Pages Required

1 page

Requirements
Nice to have
• Inspirations: https://www.qz.lo/ https://www.junebrook.example/ https://www.megaroster.example/ https://pluno.example/

```html
<!DOCTYPE html>
<html lang="en">
<head>
<meta charset="utf-8">
<title>VELMIT — Solar Client Acquisition</title>
<link href="https://fonts.googleapis.com/css2?family=Montserrat:wght@300;400&display=swap" rel="stylesheet">
<style>
:root{
  --navy:#10202d;
  --white:#ffffff;
  --text:#1d2a35;
  --field-border:#d9dde1;
  --sky-top:#5d7a93;
  --sky-warm:#d9965a;
  --panel-blue:#2c4a86;
}
*{box-sizing:border-box;margin:0;padding:0}
html,body{width:1200px;height:2183px;overflow:hidden}
body{position:relative;font-family:'Montserrat',sans-serif;font-weight:300;color:var(--text);background:var(--white)}
a{color:inherit;text-decoration:none}

/* header */
.site-header{position:absolute;left:0;top:0;width:1200px;height:83px;background:var(--navy)}
.brand{position:absolute;left:118px;top:19px;color:var(--white);font-size:36px;font-weight:300;letter-spacing:1px;line-height:44px}
.main-nav{position:absolute;top:33px;left:0;color:var(--white);font-size:15.5px;font-weight:400}
.main-nav a{position:absolute;white-space:nowrap}
.btn{position:absolute;display:flex;align-items:center;justify-content:center;border-radius:30px;font-size:15.5px;font-weight:400}
.btn-light{background:var(--white);color:var(--text)}
.btn-dark{background:var(--navy);color:var(--white)}

/* hero */
.hero{position:absolute;left:0;top:83px;width:1200px;height:647px;
  background:
   linear-gradient(160deg,rgba(16,32,45,.35) 0%,transparent 40%),
   linear-gradient(180deg,var(--sky-top) 0%,#9a8c7e 22%,var(--sky-warm) 38%,#7c6f6a 52%,#3b4f78 70%,var(--panel-blue) 100%)}
.hero-title{position:absolute;left:110px;top:120px;width:560px;color:var(--white);font-size:68px;font-weight:300;line-height:77px}
.hero-copy{position:absolute;left:110px;top:294px;width:525px;color:var(--white);font-size:26px;font-weight:300;line-height:34px}

.quote-card{position:absolute;left:646px;top:53px;width:442px;height:537px;background:var(--white);border-radius:14px;overflow:hidden}
.quote-card h2{height:54px;background:var(--navy);color:var(--white);font-size:34px;font-weight:300;text-align:center;line-height:54px;border-radius:14px}
.field{position:absolute;left:28px;width:387px;height:45px;border:1px solid var(--field-border);border-radius:6px;box-shadow:0 1px 3px rgba(0,0,0,.12);font-size:10px;font-weight:400;color:var(--text);padding:15px 0 0 27px}
.field-msg{height:137px;padding-top:17px}

/* about */
.section-title{position:absolute;font-size:41px;font-weight:300;color:var(--text)}
.body-copy{position:absolute;font-size:15.5px;line-height:25.7px;font-weight:300;color:var(--text)}
.photo{position:absolute}
.photo-about{left:582px;top:816px;width:505px;height:416px;border-radius:17px;
  background:linear-gradient(120deg,#9fa9b6 0%,#6c7d8e 35%,#c9b49a 55%,#b2322f 78%,#59422c 100%)}

/* services */
.photo-advertising{left:385px;top:1321px;width:276px;height:345px;background:linear-gradient(180deg,#a9b8c6 0%,#d88a2e 30%,#e8e3da 45%,#1a2a38 65%,#6d8a3c 100%)}
.photo-analytics{left:686px;top:1376px;width:189px;height:236px;background:linear-gradient(135deg,#2c4a86 0%,#6f86b3 50%,#d7a45a 100%)}
.photo-crm{left:899px;top:1376px;width:189px;height:236px;background:linear-gradient(180deg,#6f7c8e 0%,#d49a63 35%,#5a6170 70%,#3c4a34 100%)}
.service-label{position:absolute;font-size:22px;font-weight:300;text-align:center;line-height:34px;color:var(--text)}
.arrow-btn{position:absolute;top:1570px;width:34px;height:34px}

/* footer */
.site-footer{position:absolute;left:0;top:1805px;width:1200px;height:378px;background:var(--navy);color:var(--white)}
.footer-brand{position:absolute;left:0;top:72px;width:1200px;text-align:center;font-size:52px;font-weight:300;letter-spacing:1px;line-height:64px}
.footer-nav{position:absolute;top:195px;left:0;font-size:15.5px;font-weight:400}
.footer-nav a{position:absolute;white-space:nowrap}
.social{position:absolute;top:250px;width:22px;height:22px;background:var(--white);border-radius:3px}
.footer-rule{position:absolute;left:0;top:324px;width:1200px;height:1px;background:rgba(255,255,255,.55)}
.copyright{position:absolute;top:343px;left:0;width:1200px;text-align:center;font-size:14px;font-weight:400}
</style>
</head>
<body>

<header class="site-header">
  <div class="brand">VELMIT</div>
  <nav class="main-nav">
    <a href="#" style="left:613px">Home</a>
    <a href="#" style="left:688px">About Us</a>
    <a href="#" style="left:787px">Contact Us</a>
  </nav>
  <a href="#" class="btn btn-light" style="left:915px;top:19px;width:172px;height:43px">Contact Us</a>
</header>

<section class="hero" role="img" aria-label="Solar panel field at sunset under a warm sky">
  <h1 class="hero-title">Welcome to VELMIT</h1>
  <p class="hero-copy">Lorem ipsum dolor sit amet, consectetur adipiscing elit, sed do eiusmod tempor incididunt ut labore et dolore magna aliqua.</p>
  <a href="#" class="btn btn-light" style="left:112px;top:470px;width:206px;height:43px">Contact Us</a>

  <form class="quote-card">
    <h2>Get a Quote</h2>
    <div class="field" style="top:95px">Enter Your Name</div>
    <div class="field" style="top:156px">Enter Your Email</div>
    <div class="field" style="top:217px">Phone</div>
    <div class="field field-msg" style="top:280px">Message</div>
    <div class="btn btn-dark" style="left:136px;top:455px;width:181px;height:43px">Submit</div>
  </form>
</section>

<section class="about">
  <h2 class="section-title" style="left:112px;top:805px">About Us</h2>
  <p class="body-copy" style="left:112px;top:876px;width:412px">Lorem ipsum dolor sit amet, consectetur adipiscing elit, sed do eiusmod tempor incididunt ut labore et dolore magna aliqua. Ut enim ad minim veniam, quis nostrud exercitation ullamco laboris nisi ut aliquip ex ea commodo consequat.</p>
  <p class="body-copy" style="left:112px;top:1024px;width:412px">Duis aute irure dolor in reprehenderit in voluptate velit esse cillum dolore eu fugiat nulla pariatur. Excepteur sint occaecat cupidatat non proident, sunt in culpa qui officia deserunt mollit anim id est laborum.</p>
  <a href="#" class="btn btn-dark" style="left:115px;top:1185px;width:182px;height:43px">Read More</a>
  <div class="photo photo-about" role="img" aria-label="Two solar engineers reviewing a tablet beside solar panels"></div>
</section>

<section class="services">
  <h2 class="section-title" style="left:111px;top:1374px;font-size:34px">Our Services</h2>
  <p class="body-copy" style="left:111px;top:1436px;width:245px">Lorem ipsum dolor sit amet, onsectetur adipiscing elit, sed eiusmod tempor incididunt ut labore et dolore magna aliqua.</p>
  <svg class="arrow-btn" style="left:113px" viewBox="0 0 34 34" aria-label="Next"><circle cx="17" cy="17" r="17" fill="#10202d"/><path d="M14 10l7 7-7 7" fill="none" stroke="#fff" stroke-width="2.6" stroke-linecap="round" stroke-linejoin="round"/></svg>
  <svg class="arrow-btn" style="left:156px" viewBox="0 0 34 34" aria-label="Previous"><circle cx="17" cy="17" r="17" fill="#10202d"/><path d="M20 10l-7 7 7 7" fill="none" stroke="#fff" stroke-width="2.6" stroke-linecap="round" stroke-linejoin="round"/></svg>

  <div class="photo photo-advertising" role="img" aria-label="Smiling worker in hard hat holding a company sign"></div>
  <p class="service-label" style="left:385px;top:1674px;width:276px">Advertising</p>

  <div class="photo photo-analytics" role="img" aria-label="Hand holding a tablet with a bar chart over solar panels"></div>
  <p class="service-label" style="left:660px;top:1621px;width:240px">Data Analytics</p>

  <div class="photo photo-crm" role="img" aria-label="Rooftop terrace with solar panels and people talking at sunset"></div>
  <p class="service-label" style="left:885px;top:1621px;width:215px">Customer Relationship Management</p>
</section>

<footer class="site-footer">
  <div class="footer-brand">VELMIT</div>
  <nav class="footer-nav">
    <a href="#" style="left:470px">Home</a>
    <a href="#" style="left:546px">About Us</a>
    <a href="#" style="left:644px">Contact Us</a>
  </nav>
  <span class="social" style="left:546px" aria-label="Social link"></span>
  <span class="social" style="left:589px" aria-label="Social link"></span>
  <span class="social" style="left:632px" aria-label="Social link"></span>
  <div class="footer-rule"></div>
  <p class="copyright">Copyright © 2023 VELMIT. All rights reserved.</p>
</footer>

</body>
</html>
```